Bright Arch Group business card

Bright Arch Group is the parent company of Bright Arch Building, Bright Arch Plumbing and Bright Arch Renovating. We require a sophisticated business card that covers all aspects of the building and plumbing space without using told or construction items.

Industry/Entity Type

Construction Company

Contact Information for Business Card

Gareth Pimley
Director
0472915083
gareth@brightarch.com.au
Www.brightarch.com.au

Font styles to use
Serif
Sans Serif

Colors
3176b5
ffce3e
0692cd
34a7d8
fbee3e
faa54b

Requirements
Must have
• Logo on front
• Logo and details on rear.
Nice to have
• Maybe water mark or shadow effect with logo
Should not have
• Tools or any construction associated items

```html
<!DOCTYPE html>
<html lang="en">
<head>
<meta charset="utf-8">
<title>Bright Arch Group – Business Card</title>
<link rel="stylesheet" href="https://fonts.googleapis.com/css2?family=Open+Sans:wght@300;700&display=swap">
<style>
  :root {
    --page-bg: #8a8a8a;
    --card-front: #f4f4f4;
    --card-rear: #0c0c0c;
    --ink-dark: #2a2a2a;
    --ink-light: #f2f2f2;
    --accent: #e8892a;
    --accent-soft: #e9b48a;
  }
  * { margin: 0; padding: 0; box-sizing: border-box; }
  html, body {
    width: 1200px; height: 1000px; overflow: hidden;
    background: var(--page-bg);
    font-family: "Open Sans", Arial, sans-serif;
  }
  .canvas { position: relative; width: 1200px; height: 1000px; }
  .card {
    position: absolute; width: 560px; height: 320px;
    box-shadow: 0 10px 30px rgba(0,0,0,.35);
  }
  .card--front { left: 60px; top: 170px; background: var(--card-front); }
  .card--rear { left: 580px; top: 510px; background: var(--card-rear); color: var(--ink-light); }

  .brand {
    display: flex; align-items: center; gap: 12px;
    font-weight: 300; letter-spacing: 0.22em; text-transform: uppercase;
  }
  .brand__dot { width: 14px; height: 14px; border-radius: 50%; background: var(--accent); flex: none; }

  .card--front .brand {
    position: absolute; right: 36px; bottom: 92px;
    font-size: 22px; color: var(--ink-dark);
  }
  .card--front .web {
    position: absolute; right: 36px; bottom: 56px;
    font-size: 16px; font-weight: 700; color: var(--ink-dark);
  }

  .card--rear .brand {
    position: absolute; left: 40px; top: 58px;
    font-size: 26px; color: var(--ink-light);
  }
  .contact { position: absolute; left: 40px; top: 160px; }
  .contact__name { font-size: 18px; font-weight: 700; }
  .contact__role { font-size: 18px; font-weight: 700; color: var(--accent); margin-bottom: 12px; }
  .contact__row {
    display: flex; align-items: center; gap: 12px;
    font-size: 17px; font-weight: 700; line-height: 28px;
  }
  .contact__icon { width: 18px; height: 18px; flex: none; }
</style>
</head>
<body>
<main class="canvas">
  <section class="card card--front" aria-label="Card front">
    <div class="brand"><span class="brand__dot"></span><span>Bright Arch Group</span></div>
    <p class="web">Www.brightarch.com.au</p>
  </section>

  <section class="card card--rear" aria-label="Card rear">
    <div class="brand"><span class="brand__dot"></span><span>Bright Arch Group</span></div>
    <div class="contact">
      <p class="contact__name">Gareth Pimley</p>
      <p class="contact__role">Director</p>
      <p class="contact__row">
        <svg class="contact__icon" viewBox="0 0 24 24" aria-hidden="true"><path fill="var(--accent)" d="M6.6 10.8a15 15 0 0 0 6.6 6.6l2.2-2.2a1 1 0 0 1 1-.25 11.4 11.4 0 0 0 3.6.57 1 1 0 0 1 1 1V20a1 1 0 0 1-1 1A17 17 0 0 1 3 4a1 1 0 0 1 1-1h3.5a1 1 0 0 1 1 1c0 1.25.2 2.45.57 3.57a1 1 0 0 1-.25 1z"/></svg>
        <span>0472915083</span>
      </p>
      <p class="contact__row">
        <svg class="contact__icon" viewBox="0 0 24 24" aria-hidden="true"><rect x="2" y="5" width="20" height="14" fill="var(--accent)"/><path d="M2 5l10 8 10-8" fill="none" stroke="var(--card-rear)" stroke-width="1.6"/></svg>
        <span>gareth@brightarch.com.au</span>
      </p>
      <p class="contact__row">
        <svg class="contact__icon" viewBox="0 0 24 24" aria-hidden="true"><g fill="none" stroke="var(--accent)" stroke-width="2"><circle cx="12" cy="12" r="9"/><ellipse cx="12" cy="12" rx="4" ry="9"/><path d="M3 12h18"/></g></svg>
        <span>Www.brightarch.com.au</span>
      </p>
    </div>
  </section>
</main>
</body>
</html>
```